Church Rivers of Morning Gospel Booklet Design

We need a booklet designed that we will be printing to hand out in our community. Wording for each page will be provided and we need graphic design to produce the layouts in a format ready for print. Booklet will be 4.75" x 4.75" square and a total of 12 pages: 1 cover page front, 1 cover page back, 10 inside pages some of which will be full spread across 2 pages.

Target Market(s)

English speaking Westerners

Industry/Entity Type

Religious

Font styles to use
Serif

Colors
ffffff
85abd2
0292cd
33b8a4
5c5c5c

Requirements
Must have
• Minimalist design with clean look described in attached document
Nice to have
• Aesthetically pleasing graphics, crisp fonts, excellent turn around times
Should not have
• Effeminate design, busy look with too much graphic and text

```html
<!DOCTYPE html>
<html lang="en">
<head>
<meta charset="utf-8">
<title>Rivers of Morning – The Gospel of Jesus Christ Booklet</title>
<link rel="stylesheet" href="https://fonts.googleapis.com/css2?family=Cinzel:wght@400;500&family=Crimson+Text:ital,wght@0,400;0,600;1,400&family=Arvo&family=Open+Sans:wght@400&display=swap">
<style>
  :root {
    --bg: #dff6f4;
    --paper: #f1f2f2;
    --white: #ffffff;
    --sky: #85abd2;
    --blue: #0292cd;
    --teal: #33b8a4;
    --ink: #5c5c5c;
    --ink-dark: #3a3a3a;
    --label: #1e1e1e;
  }
  * { box-sizing: border-box; margin: 0; padding: 0; }
  html, body { width: 1138px; height: 1200px; overflow: hidden; }
  body {
    background: var(--bg);
    position: relative;
    font-family: "Crimson Text", Georgia, serif;
    color: var(--ink);
  }

  .label {
    position: absolute;
    font-family: "Open Sans", Arial, sans-serif;
    font-size: 14px;
    color: var(--label);
    letter-spacing: 0.2px;
    white-space: nowrap;
  }
  .label--center { transform: translateX(-50%); }

  .page {
    position: absolute;
    width: 233px;
    height: 234px;
    background: var(--paper);
    overflow: hidden;
  }
  .spread {
    position: absolute;
    display: flex;
    width: 456px;
    height: 236px;
  }
  .spread .page { position: relative; width: 50%; height: 100%; }
  .spread .page + .page { border-left: 1px solid #dcdede; }

  /* Cover artwork */
  .cover-sky {
    position: absolute; inset: 0;
    background:
      radial-gradient(ellipse at 30% 10%, rgba(133,171,210,0.55), transparent 60%),
      radial-gradient(ellipse at 75% 20%, rgba(51,184,164,0.28), transparent 55%),
      linear-gradient(180deg, #bfdde3 0%, #dcecef 40%, #eef3f4 70%, #f3f4f4 100%);
  }
  .cover-rule {
    position: absolute;
    left: 0; right: 0;
    top: 88%;
    height: 3px;
    background: linear-gradient(90deg, var(--teal), var(--blue));
  }
  .cover-title {
    position: absolute;
    right: 20px;
    top: 80%;
    display: flex;
    align-items: baseline;
    gap: 3px;
    background: var(--paper);
    padding-left: 2px;
    white-space: nowrap;
  }
  .cover-title__lead { font-size: 8.5px; color: var(--ink-dark); }
  .cover-title__name { font-family: "Cinzel", "Times New Roman", serif; font-size: 18px; color: var(--ink-dark); }

  /* Inner pages */
  .inner::before {
    content: ""; position: absolute; left: 0; right: 0; top: 0; height: 3px;
    background: linear-gradient(90deg, var(--teal), var(--blue));
  }
  .inner::after {
    content: ""; position: absolute; left: 0; right: 0; bottom: 0; height: 24px;
    background: linear-gradient(90deg, var(--teal), var(--blue));
  }
  .inner--right::after { background: linear-gradient(90deg, var(--blue), var(--teal)); }

  .copy {
    position: absolute;
    left: 20px; right: 20px;
    font-size: 7.2px;
    line-height: 1.45;
    text-align: center;
    color: var(--ink-dark);
  }
  .copy p + p { margin-top: 7px; }
  .copy--left { text-align: left; left: 22px; right: 22px; }
  .copy ol { padding-left: 9px; margin-top: 7px; }
  .copy li + li { margin-top: 4px; }

  .wing {
    display: block;
    width: 14px; height: 8px;
    margin: 0 auto 12px;
    border-radius: 4px 4px 7px 7px;
    background: #8a8d8d;
  }

  .photo { position: absolute; inset: 0; }
  .photo--night {
    background:
      radial-gradient(ellipse at 60% 40%, rgba(80,170,170,0.55), transparent 55%),
      radial-gradient(ellipse at 40% 60%, rgba(60,90,170,0.5), transparent 60%),
      linear-gradient(180deg, #0c1426 0%, #18304f 55%, #0a0f1a 100%);
  }
  .photo--clouds {
    background: linear-gradient(180deg, #3a6a8a 0%, #6f8fa3 35%, #b49a8e 52%, #6d7f96 65%, #3f5674 100%);
  }

  .verse {
    position: absolute; left: 0; right: 0; top: 74px;
    text-align: center;
    font-family: "Arvo", Georgia, serif;
    color: #eef3f5;
    letter-spacing: 0.8px;
  }
  .verse__line { font-size: 7.5px; line-height: 1.1; margin-bottom: 9px; }
  .verse__line--big { font-size: 13px; color: #c9d9e2; margin-bottom: 9px; }
  .verse__ref { font-size: 7.5px; margin-top: 38px; }
</style>
</head>
<body>

  <!-- Row 1 -->
  <span class="label" style="left:158px; top:149px;">FRONT COVER</span>
  <section class="page cover" style="left:310px; top:38px;">
    <div class="cover-sky" role="img" aria-label="Soft watercolour sky wash in pale blue and teal"></div>
    <div class="cover-rule"></div>
    <h1 class="cover-title"><span class="cover-title__lead">The Gospel of</span><span class="cover-title__name">JESUS CHRIST</span></h1>
  </section>

  <section class="page cover" style="left:587px; top:42px;">
    <div class="cover-sky" role="img" aria-label="Soft watercolour sky wash in pale blue and teal"></div>
    <div class="cover-rule"></div>
  </section>
  <span class="label" style="left:876px; top:149px;">BACK COVER</span>

  <!-- Row 2 -->
  <div class="spread" style="left:86px; top:323px;">
    <section class="page cover">
      <div class="cover-sky" role="img" aria-label="Soft watercolour sky wash in pale blue and teal"></div>
      <div class="cover-rule"></div>
    </section>
    <section class="page cover">
      <div class="cover-sky" role="img" aria-label="Soft watercolour sky wash in pale blue and teal"></div>
      <div class="cover-rule"></div>
      <div class="cover-title" style="right:6px; font-size:0;"><span class="cover-title__lead">The Gospel of</span><span class="cover-title__name">JESUS CHRIST</span></div>
    </section>
  </div>
  <span class="label label--center" style="left:316px; top:570px;">FRONT &amp; BACK COVER</span>

  <div class="spread" style="left:590px; top:322px;">
    <section class="page">
      <div class="photo photo--night" role="img" aria-label="Photograph of a person standing under a starry night sky with the Milky Way"></div>
    </section>
    <section class="page inner inner--right">
      <div class="copy" style="top:62px;">
        <span class="wing" role="img" aria-label="Small wing ornament"></span>
        <p>God willingly created the universe, meaning he envisioned, designed, and made us.</p>
        <p>“In the beginning God created the heavens and the earth.”<br>(Genesis 1:1)</p>
      </div>
    </section>
  </div>
  <span class="label label--center" style="left:813px; top:570px;">PAGE 2 - 3</span>

  <!-- Row 3 -->
  <div class="spread" style="left:85px; top:616px;">
    <section class="page inner">
      <div class="copy copy--left" style="top:17px;">
        <span class="wing" role="img" aria-label="Small wing ornament"></span>
        <p>This reality establishes some foundational truths for all of us:</p>
        <ol>
          <li>God loves us - he didn’t have to create us; we are here because he couldn’t imagine life without us.</li>
          <li>God is the proper authority in our lives - if he designed and made us, he rightfully owns us.</li>
          <li>God knows the purpose of our lives - if he designed and made us, he knows why we are here.</li>
          <li>God’s truth is the truth we need - if he designed and made us, he knows what it takes for life to go well for us.</li>
        </ol>
      </div>
    </section>
    <section class="page inner inner--right">
      <div class="copy" style="top:47px;">
        <span class="wing" role="img" aria-label="Small wing ornament"></span>
        <p>But we, mankind, have all rejected God’s authority in our lives. And because he rightfully owns us, our rebellion against God is a grave injustice; an act of treason for which we deserve to be cut off from God forever.</p>
        <p>“For the wages of sin is death...”<br>(Romans 6:23)</p>
      </div>
    </section>
  </div>
  <span class="label label--center" style="left:318px; top:865px;">PAGE 4 - 5</span>

  <div class="spread" style="left:590px; top:616px;">
    <section class="page inner">
      <div class="copy" style="top:52px;">
        <span class="wing" role="img" aria-label="Small wing ornament"></span>
        <p>This alienation from God is evident in a myriad of ways including poverty, crime, conflict in our relationships, and our internal struggles. But worse, when we die, we must face the consequences for our rejection of God by spending eternity in hell - a lake of fire created by God as the place where our treason is brought to justice.</p>
      </div>
    </section>
    <section class="page inner inner--right">
      <div class="copy" style="top:28px;">
        <span class="wing" role="img" aria-label="Small wing ornament"></span>
        <p>But God does not want you to pay for your own sins. God loves us so much he sent his only son to save us. Jesus Christ died on the cross to serve our sentence for our rebellion against God and rose again on the third day. Since Christ paid our full penalty, we can be completely forgiven and reconciled to God.</p>
        <p>“For God so loved the world that he sent his one and only son that whosoever believes in him will not perish but have eternal life.”<br>(John 3:16)</p>
      </div>
    </section>
  </div>
  <span class="label label--center" style="left:813px; top:865px;">PAGE 6 - 7</span>

  <!-- Row 4 -->
  <div class="spread" style="left:85px; top:910px;">
    <section class="page inner">
      <div class="copy" style="top:56px;">
        <span class="wing" role="img" aria-label="Small wing ornament"></span>
        <p>Here is what you must do to be saved:</p>
        <p style="margin-top:18px;">First, ask Jesus Christ to save you (Since he is God, he can hear you): Acknowledge that God is the rightful authority of the universe and your life. Apologize to him for your rebellion against God.</p>
      </div>
    </section>
    <section class="page inner inner--right">
      <div class="copy" style="top:45px;">
        <span class="wing" role="img" aria-label="Small wing ornament"></span>
        <p>Ask Jesus Christ to come into your life as your Lord and Savior. This decision will immediately trigger his miracle of salvation in you. God now lives in you!</p>
        <p>“If you confess with your mouth that Jesus is Lord and believe in your heart that God raised him from the dead, you will be saved.”<br>(Romans 10:9)</p>
      </div>
    </section>
  </div>
  <span class="label label--center" style="left:318px; top:1159px;">PAGE 8 - 9</span>

  <div class="spread" style="left:594px; top:910px; width:458px;">
    <section class="page inner">
      <div class="copy" style="top:55px;">
        <span class="wing" role="img" aria-label="Small wing ornament"></span>
        <p>Next, God has given us the Bible and his church as the key tools for us to grow in our understanding of God and our personal relationship with him. So, it is essential you find a local church that believes the Bible is 100% true. Tell one of the pastors you are a brand new Christian and they will help you from there.</p>
      </div>
    </section>
    <section class="page">
      <div class="photo photo--clouds" role="img" aria-label="Photograph of a sky above clouds at sunrise"></div>
      <div class="verse">
        <p class="verse__line">IF YOU CONFESS WITH YOUR MOUTH,</p>
        <p class="verse__line verse__line--big">“JESUS IS LORD,”</p>
        <p class="verse__line">AND BELIEVE IN YOUR HEART THAT</p>
        <p class="verse__line">GOD RAISED HIM FROM THE DEAD,</p>
        <p class="verse__line verse__line--big" style="color:#eef3f5;">YOU WILL BE SAVED.</p>
        <p class="verse__ref">ROMANS 10:9</p>
      </div>
    </section>
  </div>
  <span class="label label--center" style="left:822px; top:1159px;">PAGE 10 - 11</span>

</body>
</html>
```